we have the following Products we need designs for.
1: Coconut Milk 425ml
2: Coconut Cream 425g
3: Tinned Fruit Cocktail 850g
4: Tinned Sliced Peaches 850g
5: Tinned Pears. 850g
I have attached a few ideas our customer had as well as Ingredients and Nutritional Info. ( Note for Australia we need NIP to be for serving size and 100g/ml) also attached example.

Target Market(s)

Supermarkets

Requirements
Must have
• Brand Name is Corvale colours can be different

```html
<!DOCTYPE html>
<html lang="en">
<head>
<meta charset="utf-8">
<title>Corvale Premium Tinned Range – Label Set</title>
<link rel="stylesheet" href="https://fonts.googleapis.com/css2?family=Luckiest+Guy&family=Oswald:wght@400;500&family=Roboto+Condensed:wght@400;700&display=swap">
<style>
:root{
  --brand-green:#1f9a3c;
  --white:#ffffff;
  --ink:#111111;
}
*{box-sizing:border-box;margin:0;padding:0}
html,body{width:1200px;height:2182px;overflow:hidden;background:var(--white)}
body{position:relative;font-family:"Roboto Condensed",Arial,sans-serif}

.label{position:absolute;left:10px;width:1183px;height:393px;overflow:hidden;background:var(--bg)}
.label--milk{top:10px;
  --bg:radial-gradient(ellipse at 85% 10%,#f8efdf 0%,#d9bd98 30%,#9c6c43 65%,#7a4b2a 100%);
  --panel:rgba(150,150,150,.85);--panel-head:#111;--panel-text:#fff;
  --title:#111;--title-stroke:#e4b43c;--ribbon:#151515;--ribbon-text:#fff;
  --photo:radial-gradient(ellipse at 55% 35%,#ffffff 0%,#eeeae4 40%,#8a5a34 70%,#5c3a20 100%);
  --bar:#3a1a0a;--bar-text:#f0a030;--weight:#fff}
.label--cream{top:455px;
  --bg:radial-gradient(ellipse at 70% 25%,#f1e2ee 0%,#c9a6cf 35%,#6f4f94 70%,#3a2560 100%);
  --panel:rgba(150,110,200,.55);--panel-head:#2a1048;--panel-text:#fff;
  --title:#1c1a5a;--title-stroke:#d8e23a;--ribbon:#1f3f7a;--ribbon-text:#fff;
  --photo:radial-gradient(ellipse at 40% 40%,#ffffff 0%,#e9e6e4 30%,#4f8f3a 55%,#7a4a26 80%);
  --bar:#2a1a30;--bar-text:#d9d0e0;--weight:#fff}
.label--cocktail{top:898px;
  --bg:radial-gradient(ellipse at 60% 10%,#fbe1d2 0%,#f2ad92 40%,#e27a62 75%,#c9a43a 100%);
  --panel:rgba(214,176,30,.8);--panel-head:#b5122e;--panel-text:#fff;
  --title:#d0121e;--title-stroke:#ffd400;--ribbon:#9c1424;--ribbon-text:#fff;
  --photo:radial-gradient(ellipse at 50% 45%,#f5a623 0%,#e84a3a 35%,#6fae3a 60%,#ffffff 85%);
  --weight:#111}
.label--peaches{top:1342px;
  --bg:radial-gradient(ellipse at 80% 20%,#fff6ef 0%,#f7c7a6 35%,#ea7a42 70%,#d8582a 100%);
  --panel:rgba(230,100,50,.75);--panel-head:#d01a30;--panel-text:#fff;
  --title:#d81d3c;--title-stroke:#7a0d24;--ribbon:#b8102c;--ribbon-text:#fff;
  --photo:radial-gradient(ellipse at 45% 40%,#ffb347 0%,#f06a2a 45%,#c8402a 75%,#8a5a30 100%);
  --weight:#111}
.label--pears{top:1785px;
  --bg:radial-gradient(ellipse at 80% 15%,#fffbe0 0%,#f1e49a 35%,#c9ae3a 70%,#a88c22 100%);
  --panel:rgba(160,140,30,.75);--panel-head:#1f4a1e;--panel-text:#fff;
  --title:#f2e21a;--title-stroke:#2a5a1a;--ribbon:#1f4a1e;--ribbon-text:#fff;
  --photo:radial-gradient(ellipse at 50% 40%,#fff36a 0%,#f0d820 45%,#c9a818 80%,#3a7a2a 100%);
  --weight:#111}
.label--pears .front--alt{--ribbon:#c0142a}

/* nutrition panel */
.nip{position:absolute;left:77px;top:27px;width:210px;color:var(--panel-text);font-size:7.5px;line-height:1}
.nip__table{background:var(--panel);padding:0 0 4px}
.nip__servings{text-align:center;font-weight:700;font-size:9px;padding:4px 0 5px}
.nip__size{display:flex;justify-content:space-between;padding:0 8px 2px}
.nip__head{background:var(--panel-head);padding:2px 8px 3px;display:flex;justify-content:space-between;align-items:flex-end}
.nip__head small{display:block;font-size:7px}
.nip__head b{font-size:10px}
.nip__dv{text-align:right;padding:4px 12px 1px 0;border-top:2px solid var(--panel-text)}
.nip__row{display:grid;grid-template-columns:118px 42px 30px;padding:1px 8px;border-top:1px solid rgba(255,255,255,.45);height:11px}
.nip__row span:nth-child(2),.nip__row span:nth-child(3){text-align:right}
.nip__row--sub span:first-child{padding-left:18px}
.nip__row--sub2 span:first-child{padding-left:28px}
.nip__row--gap{margin-top:10px;border-top:2px solid var(--panel-text)}
.nip__trans{font-style:italic}
.nip__note{font-size:5.5px;font-style:italic;text-align:right;padding:6px 4px 0 36px;line-height:1.2}
.nip__ingr{font-size:7px;padding-top:10px;line-height:1.25}
.nip__maker{position:absolute;left:77px;top:352px;font-size:7px;font-weight:700;color:var(--panel-text)}
.nip__icons{position:absolute;left:262px;top:340px}

/* front panel */
.front{position:absolute;top:0;width:380px;height:393px}
.front--a{left:335px}
.front--b{left:780px}
.brand{position:absolute;top:20px;left:0;width:100%;display:flex;justify-content:center;align-items:center;gap:5px}
.brand__mark{width:12px;height:12px;background:var(--brand-green)}
.brand__name{font-weight:700;font-size:19px;color:var(--brand-green)}
.ribbon{position:absolute;top:70px;left:125px;width:130px;height:42px}
.title{position:absolute;top:112px;left:0;width:100%;text-align:center;font-family:"Luckiest Guy",Impact,sans-serif;color:var(--title);-webkit-text-stroke:3px var(--title-stroke);paint-order:stroke fill;line-height:.95;letter-spacing:1px}
.title span{display:block}
.title--lg{font-size:52px}
.title--md{font-size:38px}
.photo{position:absolute;left:55px;top:232px;width:270px;height:230px;border-radius:50%;background:var(--photo)}
.photo--fruit{top:245px;height:240px}
.bar{position:absolute;left:12px;top:352px;width:240px;height:18px;background:var(--bar);color:var(--bar-text);font-size:11px;letter-spacing:3px;text-align:center;line-height:18px}
.weight{position:absolute;left:265px;top:340px;color:var(--weight);font-family:"Oswald",Arial,sans-serif;font-size:29px;line-height:1}
.weight small{display:block;font-family:"Roboto Condensed",Arial,sans-serif;font-size:6px;margin-top:2px}
</style>
</head>
<body>

<svg width="0" height="0" style="position:absolute">
  <defs>
    <path id="ribbon-arc" d="M8 28 Q65 4 122 28"/>
    <symbol id="icon-recycle" viewBox="0 0 40 26">
      <g fill="none" stroke="currentColor" stroke-width="1.6">
        <path d="M3 8 h12 l-2 16 h-8 z"/><path d="M2 7 h14"/><circle cx="18" cy="4" r="2"/><path d="M18 7 v8 l-3 4"/>
        <path d="M26 2 h7 v8 a3.5 3.5 0 0 1 -7 0 z"/><path d="M29.5 13 v11"/><path d="M36 2 v22 M34 2 v6 h4 v-6"/>
      </g>
    </symbol>
  </defs>
</svg>

<!-- Coconut Milk -->
<section class="label label--milk">
  <div class="nip">
    <div class="nip__table">
      <p class="nip__servings">4 servings per container</p>
      <p class="nip__size"><span>serving size</span><span>3.38 fl. oz (100ml)</span></p>
      <div class="nip__head"><span><small>Amount Per serving</small><b>Calories</b></span><b>160</b></div>
      <p class="nip__dv">% Daily Value *</p>
      <p class="nip__row"><span>Total Fat</span><span>16 g</span><span>21 %</span></p>
      <p class="nip__row nip__row--sub"><span>Saturated Fat</span><span>17 g</span><span>76 %</span></p>
      <p class="nip__row nip__row--sub2 nip__trans"><span>Trans Fat</span><span>0 g</span><span></span></p>
      <p class="nip__row nip__row--gap"><span>Cholesterol</span><span>0 mg</span><span>0 %</span></p>
      <p class="nip__row"><span>Sodium</span><span>15 mg</span><span>1 %</span></p>
      <p class="nip__row"><span>Total Carbohydrate</span><span>3 g</span><span>1 %</span></p>
      <p class="nip__row nip__row--sub"><span>Dietary Fiber</span><span>3 g</span><span>1 %</span></p>
      <p class="nip__row nip__row--sub2"><span>Sugars</span><span>2 g</span><span>0 %</span></p>
      <p class="nip__row nip__row--sub"><span>Includes 0g Added Sugars</span><span>0%</span><span></span></p>
      <p class="nip__row nip__row--gap"><span>Protein</span><span>&lt;1 g</span><span></span></p>
      <p class="nip__row"><span>Vitamin D</span><span>0 mcg</span><span>0 %</span></p>
      <p class="nip__row"><span>Calcium</span><span>3 mg</span><span>0 %</span></p>
      <p class="nip__row"><span>Iron</span><span>0 mg</span><span>0 %</span></p>
      <p class="nip__row"><span>Potassium</span><span>125 mg</span><span>2 %</span></p>
    </div>
    <p class="nip__note">* The % Daily Values (DV) tell you how much a nutrient in a serving of food contributes to a daily diet. 2,000 calories a day is used for general advice.</p>
    <p class="nip__ingr">Ingredient: Coconut Extract (76%), Water Thickener (Guar Gum)<br>Label size: 247*99mm</p>
  </div>
  <p class="nip__maker">Manufactured by:</p>
  <svg class="nip__icons" width="40" height="26" style="color:#fff"><use href="#icon-recycle"/></svg>

  <div class="front front--a">
    <div class="brand"><span class="brand__mark"></span><span class="brand__name">Corvale</span></div>
    <svg class="ribbon" viewBox="0 0 130 42"><path d="M2 20 Q65 -6 128 20 L124 38 Q65 12 6 38 Z" fill="var(--ribbon)"/><text font-family="Oswald, sans-serif" font-size="13" letter-spacing="3" fill="var(--ribbon-text)"><textPath href="#ribbon-arc" startOffset="50%" text-anchor="middle">PREMIUM</textPath></text></svg>
    <h1 class="title title--lg"><span>COCONUT</span><span>MILK</span></h1>
    <div class="photo" role="img" aria-label="Halved coconut with a splash of coconut milk"></div>
    <p class="bar">UNSWEETENED</p>
    <p class="weight">425ml<small>3.38 fl. oz (100ml)</small></p>
  </div>
  <div class="front front--b">
    <div class="brand"><span class="brand__mark"></span><span class="brand__name">Corvale</span></div>
    <svg class="ribbon" viewBox="0 0 130 42"><path d="M2 20 Q65 -6 128 20 L124 38 Q65 12 6 38 Z" fill="var(--ribbon)"/><text font-family="Oswald, sans-serif" font-size="13" letter-spacing="3" fill="var(--ribbon-text)"><textPath href="#ribbon-arc" startOffset="50%" text-anchor="middle">PREMIUM</textPath></text></svg>
    <h1 class="title title--lg"><span>COCONUT</span><span>MILK</span></h1>
    <div class="photo" role="img" aria-label="Halved coconut with a splash of coconut milk"></div>
    <p class="bar">UNSWEETENED</p>
    <p class="weight">425ml<small>3.38 fl. oz (100ml)</small></p>
  </div>
</section>

<!-- Coconut Cream -->
<section class="label label--cream">
  <div class="nip">
    <div class="nip__table">
      <p class="nip__servings">4 servings per container</p>
      <p class="nip__size"><span>serving size</span><span>3.38 fl. oz (100ml)</span></p>
      <div class="nip__head"><span><small>Amount Per serving</small><b>Calories</b></span><b>160</b></div>
      <p class="nip__dv">% Daily Value *</p>
      <p class="nip__row"><span>Total Fat</span><span>16 g</span><span>21 %</span></p>
      <p class="nip__row nip__row--sub"><span>Saturated Fat</span><span>17 g</span><span>76 %</span></p>
      <p class="nip__row nip__row--sub2 nip__trans"><span>Trans Fat</span><span>0 g</span><span></span></p>
      <p class="nip__row nip__row--gap"><span>Cholesterol</span><span>0 mg</span><span>0 %</span></p>
      <p class="nip__row"><span>Sodium</span><span>15 mg</span><span>1 %</span></p>
      <p class="nip__row"><span>Total Carbohydrate</span><span>3 g</span><span>1 %</span></p>
      <p class="nip__row nip__row--sub"><span>Dietary Fiber</span><span>3 g</span><span>1 %</span></p>
      <p class="nip__row nip__row--sub2"><span>Sugars</span><span>2 g</span><span>0 %</span></p>
      <p class="nip__row nip__row--sub"><span>Includes 0g Added Sugars</span><span>0%</span><span></span></p>
      <p class="nip__row nip__row--gap"><span>Protein</span><span>&lt;1 g</span><span></span></p>
      <p class="nip__row"><span>Vitamin D</span><span>0 mcg</span><span>0 %</span></p>
      <p class="nip__row"><span>Calcium</span><span>3 mg</span><span>0 %</span></p>
      <p class="nip__row"><span>Iron</span><span>0 mg</span><span>0 %</span></p>
      <p class="nip__row"><span>Potassium</span><span>125 mg</span><span>2 %</span></p>
    </div>
    <p class="nip__note">* The % Daily Values (DV) tell you how much a nutrient in a serving of food contributes to a daily diet. 2,000 calories a day is used for general advice.</p>
    <p class="nip__ingr">Ingredient: Coconut Extract (76%), Water Thickener (Guar Gum)<br>Label size: 247*99mm</p>
  </div>
  <p class="nip__maker">Manufactured by:</p>
  <svg class="nip__icons" width="40" height="26" style="color:#fff"><use href="#icon-recycle"/></svg>

  <div class="front front--a">
    <div class="brand"><span class="brand__mark"></span><span class="brand__name">Corvale</span></div>
    <svg class="ribbon" viewBox="0 0 130 42"><path d="M2 20 Q65 -6 128 20 L124 38 Q65 12 6 38 Z" fill="var(--ribbon)"/><text font-family="Oswald, sans-serif" font-size="13" letter-spacing="3" fill="var(--ribbon-text)"><textPath href="#ribbon-arc" startOffset="50%" text-anchor="middle">PREMIUM</textPath></text></svg>
    <h1 class="title title--lg"><span>COCONUT</span><span>CREAM</span></h1>
    <div class="photo" role="img" aria-label="Coconut with palm leaves and a cream splash"></div>
    <p class="bar">UNSWEETENED</p>
    <p class="weight">425g<small>3.38 fl. oz (100ml)</small></p>
  </div>
  <div class="front front--b">
    <div class="brand"><span class="brand__mark"></span><span class="brand__name">Corvale</span></div>
    <svg class="ribbon" viewBox="0 0 130 42"><path d="M2 20 Q65 -6 128 20 L124 38 Q65 12 6 38 Z" fill="var(--ribbon)"/><text font-family="Oswald, sans-serif" font-size="13" letter-spacing="3" fill="var(--ribbon-text)"><textPath href="#ribbon-arc" startOffset="50%" text-anchor="middle">PREMIUM</textPath></text></svg>
    <h1 class="title title--lg"><span>COCONUT</span><span>CREAM</span></h1>
    <div class="photo" role="img" aria-label="Coconut with palm leaves and a cream splash"></div>
    <p class="bar">UNSWEETENED</p>
    <p class="weight">425g<small>3.38 fl. oz (100ml)</small></p>
  </div>
</section>

<!-- Fruit Cocktail -->
<section class="label label--cocktail">
  <div class="nip">
    <div class="nip__table">
      <p class="nip__servings">4 servings per container</p>
      <p class="nip__size"><span>serving size</span><span>3.38 fl. oz (100ml)</span></p>
      <div class="nip__head"><span><small>Amount Per serving</small><b>Calories</b></span><b>160</b></div>
      <p class="nip__dv">% Daily Value *</p>
      <p class="nip__row"><span>Total Fat</span><span>16 g</span><span>21 %</span></p>
      <p class="nip__row nip__row--sub"><span>Saturated Fat</span><span>17 g</span><span>76 %</span></p>
      <p class="nip__row nip__row--sub2 nip__trans"><span>Trans Fat</span><span>0 g</span><span></span></p>
      <p class="nip__row nip__row--gap"><span>Cholesterol</span><span>0 mg</span><span>0 %</span></p>
      <p class="nip__row"><span>Sodium</span><span>15 mg</span><span>1 %</span></p>
      <p class="nip__row"><span>Total Carbohydrate</span><span>3 g</span><span>1 %</span></p>
      <p class="nip__row nip__row--sub"><span>Dietary Fiber</span><span>3 g</span><span>1 %</span></p>
      <p class="nip__row nip__row--sub2"><span>Sugars</span><span>2 g</span><span>0 %</span></p>
      <p class="nip__row nip__row--sub"><span>Includes 0g Added Sugars</span><span>0%</span><span></span></p>
      <p class="nip__row nip__row--gap"><span>Protein</span><span>&lt;1 g</span><span></span></p>
      <p class="nip__row"><span>Vitamin D</span><span>0 mcg</span><span>0 %</span></p>
      <p class="nip__row"><span>Calcium</span><span>3 mg</span><span>0 %</span></p>
      <p class="nip__row"><span>Iron</span><span>0 mg</span><span>0 %</span></p>
      <p class="nip__row"><span>Potassium</span><span>125 mg</span><span>2 %</span></p>
    </div>
    <p class="nip__note">* The % Daily Values (DV) tell you how much a nutrient in a serving of food contributes to a daily diet. 2,000 calories a day is used for general advice.</p>
    <p class="nip__ingr">Ingredient: Coconut Extract (76%), Water Thickener (Guar Gum)<br>Label size: 247*99mm</p>
  </div>
  <p class="nip__maker">Manufactured by:</p>
  <svg class="nip__icons" width="40" height="26" style="color:#fff"><use href="#icon-recycle"/></svg>

  <div class="front front--a">
    <div class="brand"><span class="brand__mark"></span><span class="brand__name">Corvale</span></div>
    <svg class="ribbon" viewBox="0 0 130 42"><path d="M2 20 Q65 -6 128 20 L124 38 Q65 12 6 38 Z" fill="var(--ribbon)"/><text font-family="Oswald, sans-serif" font-size="13" letter-spacing="3" fill="var(--ribbon-text)"><textPath href="#ribbon-arc" startOffset="50%" text-anchor="middle">PREMIUM</textPath></text></svg>
    <h1 class="title title--md" style="top:118px"><span>TINNED FRUIT</span><span style="font-size:46px">COCKTAIL</span></h1>
    <div class="photo photo--fruit" role="img" aria-label="White bowl of mixed fruit salad"></div>
    <p class="weight">850g<small>3.38 fl. oz (100ml)</small></p>
  </div>
  <div class="front front--b">
    <div class="brand"><span class="brand__mark"></span><span class="brand__name">Corvale</span></div>
    <svg class="ribbon" viewBox="0 0 130 42"><path d="M2 20 Q65 -6 128 20 L124 38 Q65 12 6 38 Z" fill="var(--ribbon)"/><text font-family="Oswald, sans-serif" font-size="13" letter-spacing="3" fill="var(--ribbon-text)"><textPath href="#ribbon-arc" startOffset="50%" text-anchor="middle">PREMIUM</textPath></text></svg>
    <h1 class="title title--md" style="top:118px"><span>TINNED FRUIT</span><span style="font-size:46px">COCKTAIL</span></h1>
    <div class="photo photo--fruit" role="img" aria-label="White bowl of mixed fruit salad"></div>
    <p class="weight">850g<small>3.38 fl. oz (100ml)</small></p>
  </div>
</section>

<!-- Sliced Peaches -->
<section class="label label--peaches">
  <div class="nip" style="left:98px">
    <div class="nip__table">
      <p class="nip__servings">4 servings per container</p>
      <p class="nip__size"><span>serving size</span><span>3.38 fl. oz (100ml)</span></p>
      <div class="nip__head"><span><small>Amount Per serving</small><b>Calories</b></span><b>160</b></div>
      <p class="nip__dv">% Daily Value *</p>
      <p class="nip__row"><span>Total Fat</span><span>16 g</span><span>21 %</span></p>
      <p class="nip__row nip__row--sub"><span>Saturated Fat</span><span>17 g</span><span>76 %</span></p>
      <p class="nip__row nip__row--sub2 nip__trans"><span>Trans Fat</span><span>0 g</span><span></span></p>
      <p class="nip__row nip__row--gap"><span>Cholesterol</span><span>0 mg</span><span>0 %</span></p>
      <p class="nip__row"><span>Sodium</span><span>15 mg</span><span>1 %</span></p>
      <p class="nip__row"><span>Total Carbohydrate</span><span>3 g</span><span>1 %</span></p>
      <p class="nip__row nip__row--sub"><span>Dietary Fiber</span><span>3 g</span><span>1 %</span></p>
      <p class="nip__row nip__row--sub2"><span>Sugars</span><span>2 g</span><span>0 %</span></p>
      <p class="nip__row nip__row--sub"><span>Includes 0g Added Sugars</span><span>0%</span><span></span></p>
      <p class="nip__row nip__row--gap"><span>Protein</span><span>&lt;1 g</span><span></span></p>
      <p class="nip__row"><span>Vitamin D</span><span>0 mcg</span><span>0 %</span></p>
      <p class="nip__row"><span>Calcium</span><span>3 mg</span><span>0 %</span></p>
      <p class="nip__row"><span>Iron</span><span>0 mg</span><span>0 %</span></p>
      <p class="nip__row"><span>Potassium</span><span>125 mg</span><span>2 %</span></p>
    </div>
    <p class="nip__note">* The % Daily Values (DV) tell you how much a nutrient in a serving of food contributes to a daily diet. 2,000 calories a day is used for general advice.</p>
    <p class="nip__ingr">Ingredient: Coconut Extract (76%), Water Thickener (Guar Gum)<br>Label size: 247*99mm</p>
  </div>
  <p class="nip__maker" style="left:98px">Manufactured by:</p>
  <svg class="nip__icons" width="40" height="26" style="color:#fff;left:282px"><use href="#icon-recycle"/></svg>

  <div class="front front--a" style="left:345px">
    <div class="brand"><span class="brand__mark"></span><span class="brand__name">Corvale</span></div>
    <svg class="ribbon" viewBox="0 0 130 42"><path d="M2 20 Q65 -6 128 20 L124 38 Q65 12 6 38 Z" fill="var(--ribbon)"/><text font-family="Oswald, sans-serif" font-size="13" letter-spacing="3" fill="var(--ribbon-text)"><textPath href="#ribbon-arc" startOffset="50%" text-anchor="middle">PREMIUM</textPath></text></svg>
    <h1 class="title title--md" style="top:118px"><span>TINNED SLICED</span><span style="font-size:50px">PEACHES</span></h1>
    <div class="photo" style="top:212px;height:240px" role="img" aria-label="Whole and halved ripe peaches"></div>
    <p class="weight">850g<small>3.38 fl. oz (100ml)</small></p>
  </div>
  <div class="front front--b" style="left:760px">
    <div class="brand"><span class="brand__mark"></span><span class="brand__name">Corvale</span></div>
    <svg class="ribbon" viewBox="0 0 130 42"><path d="M2 20 Q65 -6 128 20 L124 38 Q65 12 6 38 Z" fill="var(--ribbon)"/><text font-family="Oswald, sans-serif" font-size="13" letter-spacing="3" fill="var(--ribbon-text)"><textPath href="#ribbon-arc" startOffset="50%" text-anchor="middle">PREMIUM</textPath></text></svg>
    <h1 class="title title--md" style="top:118px"><span>TINNED SLICED</span><span style="font-size:50px">PEACHES</span></h1>
    <div class="photo" style="top:212px;height:240px" role="img" aria-label="Whole and halved ripe peaches"></div>
    <p class="weight">850g<small>3.38 fl. oz (100ml)</small></p>
  </div>
</section>

<!-- Pears -->
<section class="label label--pears">
  <div class="nip" style="left:108px">
    <div class="nip__table">
      <p class="nip__servings">4 servings per container</p>
      <p class="nip__size"><span>serving size</span><span>3.38 fl. oz (100ml)</span></p>
      <div class="nip__head"><span><small>Amount Per serving</small><b>Calories</b></span><b>160</b></div>
      <p class="nip__dv">% Daily Value *</p>
      <p class="nip__row"><span>Total Fat</span><span>16 g</span><span>21 %</span></p>
      <p class="nip__row nip__row--sub"><span>Saturated Fat</span><span>17 g</span><span>76 %</span></p>
      <p class="nip__row nip__row--sub2 nip__trans"><span>Trans Fat</span><span>0 g</span><span></span></p>
      <p class="nip__row nip__row--gap"><span>Cholesterol</span><span>0 mg</span><span>0 %</span></p>
      <p class="nip__row"><span>Sodium</span><span>15 mg</span><span>1 %</span></p>
      <p class="nip__row"><span>Total Carbohydrate</span><span>3 g</span><span>1 %</span></p>
      <p class="nip__row nip__row--sub"><span>Dietary Fiber</span><span>3 g</span><span>1 %</span></p>
      <p class="nip__row nip__row--sub2"><span>Sugars</span><span>2 g</span><span>0 %</span></p>
      <p class="nip__row nip__row--sub"><span>Includes 0g Added Sugars</span><span>0%</span><span></span></p>
      <p class="nip__row nip__row--gap"><span>Protein</span><span>&lt;1 g</span><span></span></p>
      <p class="nip__row"><span>Vitamin D</span><span>0 mcg</span><span>0 %</span></p>
      <p class="nip__row"><span>Calcium</span><span>3 mg</span><span>0 %</span></p>
      <p class="nip__row"><span>Iron</span><span>0 mg</span><span>0 %</span></p>
      <p class="nip__row"><span>Potassium</span><span>125 mg</span><span>2 %</span></p>
    </div>
    <p class="nip__note">* The % Daily Values (DV) tell you how much a nutrient in a serving of food contributes to a daily diet. 2,000 calories a day is used for general advice.</p>
    <p class="nip__ingr">Ingredient: Coconut Extract (76%), Water Thickener (Guar Gum)<br>Label size: 247*99mm</p>
  </div>
  <p class="nip__maker" style="left:108px">Manufactured by:</p>
  <svg class="nip__icons" width="40" height="26" style="color:#fff;left:292px"><use href="#icon-recycle"/></svg>

  <div class="front front--a" style="left:355px">
    <div class="brand"><span class="brand__mark"></span><span class="brand__name">Corvale</span></div>
    <svg class="ribbon" viewBox="0 0 130 42"><path d="M2 20 Q65 -6 128 20 L124 38 Q65 12 6 38 Z" fill="var(--ribbon)"/><text font-family="Oswald, sans-serif" font-size="13" letter-spacing="3" fill="var(--ribbon-text)"><textPath href="#ribbon-arc" startOffset="50%" text-anchor="middle">PREMIUM</textPath></text></svg>
    <h1 class="title title--lg" style="top:118px;font-size:50px"><span>TINNED</span><span>PEARS</span></h1>
    <div class="photo" style="left:80px;width:220px;top:235px;height:230px" role="img" aria-label="Whole yellow pear with a halved slice"></div>
    <p class="weight">850g<small>3.38 fl. oz (100ml)</small></p>
  </div>
  <div class="front front--b front--alt" style="left:762px">
    <div class="brand"><span class="brand__mark"></span><span class="brand__name">Corvale</span></div>
    <svg class="ribbon" viewBox="0 0 130 42"><path d="M2 20 Q65 -6 128 20 L124 38 Q65 12 6 38 Z" fill="var(--ribbon)"/><text font-family="Oswald, sans-serif" font-size="13" letter-spacing="3" fill="var(--ribbon-text)"><textPath href="#ribbon-arc" startOffset="50%" text-anchor="middle">PREMIUM</textPath></text></svg>
    <h1 class="title title--lg" style="top:118px;font-size:50px"><span>TINNED</span><span>PEARS</span></h1>
    <div class="photo" style="left:80px;width:220px;top:235px;height:230px" role="img" aria-label="Whole yellow pear with a halved slice"></div>
    <p class="weight">850g<small>3.38 fl. oz (100ml)</small></p>
  </div>
</section>

</body>
</html>
```